Radiant Crossing - An Exciting Mission & Book Cover Project

Help me to inspire people to live their best life! This is a mission, not just a design project.
I need a Book Cover designed to keep me inspired on the process of writing my book.
Book Title: Radiant Crossing
Tag Line: Three Simple Steps to get out of your own way, SuperCharge your Life and Step into Purpose!
Author: Marlis Quenby

The three steps are: Ownership, Vision and Action (Not sure if this should be on the front or back of the book cover)

The book is a self-help, motivational book. Personal development.
The cover needs to be strong and capture peoples attention, especially with competing shelf space. I almost see a fire ball of flame or explosion that will grab peoples attention.
My company is The Lantern Institute. I have added the company logo and a few pages of my presentation and topic outline to give an idea.
Maybe: The Lantern Institute logo on back of the cover. website is marlisquenby.com

THOUGHT: People should be able to take a photo of them holding the book cover showing what area of life they want Radiant Crossing in. This is why the front cover must be so visual and powerful that they want to take a photo with it. Ie. Explosion, fire, strong and bold.

Target Market(s)

Anyone who feels stuck and needs to breakthrough and move forward in life.

Industry/Entity Type

Motivation

Font styles to use
Serif
Sans Serif

Colors
ec1f27
f37122
fbed22

Requirements
Must have
• The design must be STRONG, SIMPLE, STAND OUT ON BOOK SHELVES.
Must have an open file to swap the photo and copy out.

Back Cover Page
1) Summary
2) 2-3 testimonials. One sentence.
3) About the Author (maybe with photo)
4) Lantern Institute logo
5) Website: radiantcrossing.com and marlisquenby.com
Nice to have
• If my photo works somewhere that would be great. I will change the photo later.
Added Where's Your Harbor? a nice cover example.
Should not have
• Right now I am writing the summary for the back of the cover. For now use Loreum Ipsum text and 2-3 recommendations. Again, I will get these only later.

```html
<!DOCTYPE html>
<html lang="en">
<head>
<meta charset="utf-8">
<title>Radiant Crossing — Book Cover</title>
<link rel="stylesheet" href="https://fonts.googleapis.com/css2?family=Alegreya+Sans+SC:wght@500;700&display=swap">
<style>
  :root {
    --page-bg: #f1f1f1;
    --flame-red: #ec1f27;
    --flame-orange: #f37122;
    --flame-yellow: #fbed22;
    --flame-gold: #f6a72e;
    --ember-dark: #6b2a14;
    --cover-ink: #ffffff;
  }
  * { box-sizing: border-box; margin: 0; padding: 0; }
  html, body {
    width: 1200px;
    height: 800px;
    overflow: hidden;
    background: var(--page-bg);
  }
  body {
    display: flex;
    align-items: center;
    justify-content: center;
    font-family: "Alegreya Sans SC", sans-serif;
  }
  .book-cover {
    position: relative;
    width: 480px;
    height: 720px;
    overflow: hidden;
    color: var(--cover-ink);
  }
  .cover-artwork {
    position: absolute;
    inset: 0;
    width: 100%;
    height: 100%;
    display: block;
  }
  .author-name {
    position: absolute;
    top: 34px;
    left: 0;
    right: 0;
    text-align: center;
    font-weight: 500;
    font-size: 24px;
    letter-spacing: 0.04em;
  }
  .book-title {
    position: absolute;
    top: 272px;
    left: 0;
    right: 0;
    text-align: center;
    font-weight: 500;
    line-height: 1;
  }
  .book-title .title-line {
    display: block;
  }
  .book-title .title-line--first {
    font-size: 76px;
    letter-spacing: 0.08em;
  }
  .book-title .title-line--second {
    margin-top: 10px;
    font-size: 58px;
    letter-spacing: 0.06em;
  }
  .publisher-mark {
    position: absolute;
    bottom: 40px;
    left: 0;
    right: 0;
    display: flex;
    align-items: center;
    justify-content: center;
    gap: 8px;
    font-weight: 500;
    font-size: 17px;
    letter-spacing: 0.04em;
    color: var(--cover-ink);
  }
  .publisher-mark .publisher-dot {
    width: 10px;
    height: 10px;
    border-radius: 50%;
    background: var(--cover-ink);
  }
</style>
</head>
<body>
  <main class="book-cover">
    <svg class="cover-artwork" viewBox="0 0 480 720" preserveAspectRatio="none" role="img" aria-label="Abstract burst of red, orange and yellow extruded blocks radiating outward from the centre like an explosion">
      <defs>
        <radialGradient id="burst" cx="50%" cy="52%" r="75%">
          <stop offset="0%" stop-color="#f15a2b"/>
          <stop offset="25%" stop-color="var(--flame-orange)"/>
          <stop offset="55%" stop-color="var(--flame-gold)"/>
          <stop offset="80%" stop-color="#f08a2a"/>
          <stop offset="100%" stop-color="var(--flame-red)"/>
        </radialGradient>
        <linearGradient id="warmth" x1="0" y1="0" x2="0" y2="1">
          <stop offset="0%" stop-color="#f7b23b" stop-opacity="0.35"/>
          <stop offset="50%" stop-color="var(--flame-red)" stop-opacity="0.35"/>
          <stop offset="100%" stop-color="#f9c23a" stop-opacity="0.3"/>
        </linearGradient>
      </defs>
      <rect width="480" height="720" fill="url(#burst)"/>
      <rect width="480" height="720" fill="url(#warmth)"/>
    </svg>

    <p class="author-name">Marlis Quenby</p>

    <h1 class="book-title">
      <span class="title-line title-line--first">Radiant</span>
      <span class="title-line title-line--second">Crossing</span>
    </h1>

    <div class="publisher-mark">
      <span class="publisher-dot"></span>
      <span class="publisher-name">The Lantern Institute</span>
    </div>
  </main>
</body>
</html>
```